Student project platform needs an awareness flyer

Tunvelo is a matchmaking and crowdfunding site for student projects. On this platform, students can team up with each other to invent a new product, innovate, or start a business. They can also raise funds for their project.

** I am in need of an 8x11" flyer to print and distribute digitally which notifies students of all different skill sets that this site exists.

The flyer should communicate that a diverse user base is being built on this site, with people who have skills in programming, engineering, design, business, finance, and so on.

The flyer should also be clean and modern, with an emphasis on creativity and innovation. I've attached the business' logo to give you an idea of the artistic style we have already established.

Target Market(s)

University students

Industry/Entity Type

Crowdfunding

Font styles to use
Serif
Sans Serif

Requirements
Must have
• * Clean and modern design
• * Color scheme of my logo: #336699 and #669933 (blue and green)
• * Convey that this site is for people of different skill sets: programming, engineering, design, business, finance, and so on.
• * See the attached "Tunvelo Copy.txt" for text to include on the flyer

```html
<!DOCTYPE html>
<html lang="en">
<head>
<meta charset="UTF-8">
<title>Tunvelo – Student Flyer</title>
<link href="https://fonts.googleapis.com/css2?family=Quicksand:wght@400;500&family=Montserrat:wght@700&family=PT+Sans:wght@400;700&display=swap" rel="stylesheet">
<style>
  :root {
    --blue: #336699;
    --blue-light: #6f9bc8;
    --green: #669933;
    --green-light: #7fb24a;
    --ink: #4a4f57;
    --page: #ece8ec;
    --paper: #ffffff;
  }
  * { margin: 0; padding: 0; box-sizing: border-box; }
  html, body { width: 1200px; height: 1037px; overflow: hidden; background: var(--page); }
  .flyer {
    position: absolute; left: 240px; top: 38px;
    width: 720px; height: 960px;
    background: linear-gradient(160deg, #f7f8f9 0%, #ffffff 45%, #f3f4f6 100%);
    box-shadow: 0 10px 30px rgba(60, 40, 60, 0.18);
    overflow: hidden;
  }
  .wave { position: absolute; left: 0; width: 720px; display: block; }
  .wave--top { top: 0; height: 200px; }
  .wave--bottom { bottom: 0; height: 80px; }

  .brand { position: absolute; right: 56px; top: 88px; display: flex; flex-direction: column; align-items: center; gap: 8px; }
  .brand__dot { width: 60px; height: 60px; border-radius: 50%; background: var(--blue-light); }
  .brand__name { font-family: 'Montserrat', sans-serif; font-weight: 700; font-size: 38px; color: var(--blue); letter-spacing: 1px; line-height: 1; }

  .callout { position: absolute; left: 70px; top: 208px; font-family: 'Quicksand', sans-serif; font-weight: 500; line-height: 1; }
  .callout__line1 { font-size: 42px; color: var(--blue-light); }
  .callout__line2 { font-size: 42px; color: var(--green-light); margin-top: 4px; }
  .rule { position: absolute; left: 70px; top: 302px; width: 590px; height: 2px; background: var(--blue); }

  .goals { position: absolute; left: 40px; top: 318px; list-style: none; }
  .goals li { display: flex; align-items: center; gap: 18px; height: 54px; font-family: 'Montserrat', sans-serif; font-weight: 700; font-size: 40px; color: var(--blue); white-space: nowrap; }
  .goals .bar { display: inline-block; height: 28px; background: var(--green-light); }
  .goals li:nth-child(1) { margin-left: 8px; } .goals li:nth-child(1) .bar { width: 28px; }
  .goals li:nth-child(2) { margin-left: 16px; } .goals li:nth-child(2) .bar { width: 40px; }
  .goals li:nth-child(3) { margin-left: 24px; } .goals li:nth-child(3) .bar { width: 52px; }
  .goals li:nth-child(4) { margin-left: 32px; } .goals li:nth-child(4) .bar { width: 70px; }

  .art-steps {
    position: absolute; left: 450px; top: 322px; width: 240px; height: 146px;
    background: linear-gradient(90deg, #d8363a 0%, #d8363a 34%, #e6e6e6 44%, #c9c9c9 100%);
    opacity: 0.85;
  }

  .banner {
    position: absolute; left: 0; top: 540px; width: 600px; height: 104px;
    background: linear-gradient(180deg, var(--green-light), var(--green));
    padding: 16px 40px 0 48px;
    font-family: 'PT Sans', sans-serif; font-weight: 700; font-size: 27px; line-height: 1.35; color: #fff;
    white-space: nowrap;
  }
  .banner__disc {
    position: absolute; left: 570px; top: 518px; width: 146px; height: 146px; border-radius: 50%;
    background: #fff; border: 3px solid #d9dde2; box-shadow: 0 3px 10px rgba(0,0,0,0.12);
  }

  .about { position: absolute; left: 70px; top: 668px; width: 450px; }
  .about__kicker { font-family: 'Quicksand', sans-serif; font-weight: 500; font-size: 38px; color: var(--green-light); line-height: 1; }
  .about__title { font-family: 'Montserrat', sans-serif; font-weight: 700; font-size: 40px; color: var(--blue); line-height: 1.05; }
  .about__text { margin-top: 10px; font-family: 'PT Sans', sans-serif; font-size: 18px; line-height: 1.65; color: var(--ink); }

  .art-cycle {
    position: absolute; left: 535px; top: 690px; width: 160px; height: 160px; border-radius: 12px;
    background: radial-gradient(circle at 50% 60%, #7fa889 0%, #c9d9cf 55%, #eef1f2 100%);
  }
</style>
</head>
<body>
  <main class="flyer">
    <svg class="wave wave--top" viewBox="0 0 720 200" preserveAspectRatio="none" aria-hidden="true">
      <defs>
        <linearGradient id="topBlue" x1="0" y1="0" x2="1" y2="1">
          <stop offset="0" stop-color="#5d8fc4"/><stop offset="1" stop-color="#8fb3d9"/>
        </linearGradient>
      </defs>
      <path d="M0 0 H720 V118 C520 62 250 58 0 150 Z" fill="url(#topBlue)"/>
      <path d="M0 150 C250 58 520 62 720 118 V140 C520 88 250 86 0 172 Z" fill="#7fb24a"/>
    </svg>

    <div class="brand">
      <span class="brand__dot"></span>
      <span class="brand__name">TUNVELO</span>
    </div>

    <div class="callout">
      <p class="callout__line1">Calling all students</p>
      <p class="callout__line2">who want to</p>
    </div>
    <div class="rule"></div>

    <ul class="goals">
      <li><span class="bar"></span>BUILD</li>
      <li><span class="bar"></span>INNOVATE</li>
      <li><span class="bar"></span>INVENT OR</li>
      <li><span class="bar"></span>START A BUSINESS</li>
    </ul>

    <div class="art-steps" role="img" aria-label="Silhouettes of business people standing on rising steps, the leader on a red block"></div>

    <div class="banner">Join Tunvelo to support and lend<br>your skills to student projects!</div>
    <div class="banner__disc"></div>

    <section class="about">
      <p class="about__kicker">What is</p>
      <h2 class="about__title">TUNVELO?</h2>
      <p class="about__text">Tunvelo is a matchmaking and crowdfunding platform for student projects. It allows students to form teams of diverse skills and raise money to build, innovate, invent, or start a business.</p>
    </section>

    <div class="art-cycle" role="img" aria-label="Cycle icon showing a light bulb, a team of people and a money bag joined by arrows"></div>

    <svg class="wave wave--bottom" viewBox="0 0 720 80" preserveAspectRatio="none" aria-hidden="true">
      <path d="M0 34 C220 10 500 10 720 26 V34 C500 20 220 22 0 44 Z" fill="#7fb24a"/>
      <path d="M0 48 C220 26 500 24 720 38 V80 H0 Z" fill="#336699"/>
      <path d="M0 70 C240 52 500 50 720 60 V80 H0 Z" fill="#ffffff"/>
    </svg>
  </main>
</body>
</html>
```